Natural Skin Care e commerce website

we are the distributor for natural skincare product , we would like to develop a e commerce website which encompass the ability to divide the product into face, body , baby , and base on ingredient , best seller, we are Verdel certified product the key point to focus is natural organic , no nasties, vegan , unpolluted , full of natural ingredient. manuka, olive nordic style temporary style website is preferred. the website name is Kolbavi store.co , the web must have ability to take the order and let the brand upload their products

```html
<!DOCTYPE html>
<html lang="en">
<head>
<meta charset="utf-8">
<title>Kolbavi Store – Natural Skincare</title>
<link href="https://fonts.googleapis.com/css2?family=Great+Vibes&family=Roboto:wght@300;400;500;700&display=swap" rel="stylesheet">
<style>
:root{
  --green:#7cb342;
  --green-dark:#5f9230;
  --ink:#333333;
  --muted:#8a8a8a;
  --page:#ffffff;
  --soft:#f6f6f4;
  --tile-blue:#eef1fd;
  --tile-lime:#e3ecc8;
  --tile-mint:#c8eac3;
  --tile-peach:#fdf2ea;
  --tile-pink:#fde6e8;
  --tile-beige:#f3e6d6;
  --sale:#c0504d;
  --star:#f2b01e;
  --footer:#3a3a3a;
  --footer-text:#b8b8b8;
}
*{box-sizing:border-box;margin:0;padding:0}
html,body{width:1200px;height:3192px;overflow:hidden}
body{position:relative;background:var(--page);font-family:'Roboto',sans-serif;color:var(--ink)}
.abs{position:absolute}
.script{font-family:'Great Vibes',cursive;font-weight:400}

/* header */
.site-header{left:0;top:0;width:1200px;height:56px;background:#fff;z-index:3}
.logo{left:240px;top:13px;font-size:26px;font-weight:700;color:var(--green-dark);display:flex;align-items:center;gap:8px}
.logo .mark{width:10px;height:10px;border-radius:50%;background:var(--green)}
.main-nav{left:528px;top:20px;display:flex;gap:22px;font-size:13px}
.main-nav a{color:var(--ink);text-decoration:none}
.main-nav a.active{color:var(--green)}
.header-icons{left:866px;top:18px;display:flex;gap:22px}

/* hero */
.hero{left:0;top:56px;width:1200px;height:492px;background:linear-gradient(90deg,#f7f6f2 0%,#eef0e6 30%,#e8d6c7 55%,#d9b7a0 75%,#ecdccc 100%)}
.hero-title{left:0;width:1200px;top:188px;text-align:center;font-size:80px;line-height:100px;color:var(--green)}
.hero-sub{left:0;width:1200px;text-align:center;top:292px;font-size:16px;color:#fff;line-height:22px}
.hero-sub strong{font-size:22px;font-weight:500}
.btn-shop{left:555px;top:382px;width:90px;height:30px;background:#fff;color:var(--ink);font-size:12px;font-weight:500;display:flex;align-items:center;justify-content:center}

/* categories */
.tile{display:flex;flex-direction:column;justify-content:center;font-size:15px;line-height:19px;padding:0 22px}
.tile.big{font-size:22px;line-height:28px;color:var(--green-dark)}
.tile-photo{background:linear-gradient(160deg,#6e7a48,#a89068 45%,#5b6a3a);color:#fff;justify-content:flex-end;align-items:center;text-align:center;padding-bottom:118px}

/* section titles */
.section-title{left:0;width:1200px;text-align:center;font-size:26px;font-weight:500}

/* product card */
.product{width:168px}
.product .thumb{position:relative;width:168px;height:200px}
.product .sale{position:absolute;left:16px;top:0;width:20px;height:58px;background:var(--sale);color:#fff;font-size:9px;writing-mode:vertical-rl;transform:rotate(180deg);display:flex;align-items:center;justify-content:center;letter-spacing:1px}
.product .name{margin-top:14px;font-size:14px;font-weight:500}
.product .stars{margin-top:6px;color:var(--star);font-size:12px;letter-spacing:1px}
.product .price{margin-top:6px;font-size:11px;color:var(--muted);display:flex;align-items:center;gap:8px}
.product .price b{color:var(--ink);font-weight:500}
.cart-dot{width:22px;height:22px;border-radius:50%;background:var(--green);display:flex;align-items:center;justify-content:center}
.hover-frame{position:absolute;inset:10px;border:6px solid #fff}
.btn-cart{position:absolute;left:34px;top:14px;width:100px;height:24px;border-radius:12px;background:var(--green);color:#fff;font-size:10px;display:flex;align-items:center;justify-content:center}
.dots{left:582px;top:1412px;display:flex;gap:8px}
.dots span{width:6px;height:6px;border-radius:50%;background:#d6d6d6}
.dots span.on{background:var(--green)}

/* banner */
.banner{left:0;top:1484px;width:1200px;height:516px;background:linear-gradient(90deg,#b9cf9a 0%,#9bbb6c 35%,#8fae62 55%,#c8a88e 75%,#a48a6c 100%)}
.banner-kicker{left:0;width:1200px;top:1680px;text-align:center;padding-left:220px;font-size:14px;letter-spacing:2px;color:#fff}
.banner-title{left:0;width:1200px;top:1700px;text-align:center;font-size:86px;line-height:104px;color:#fff}
.banner-copy{left:0;width:1200px;top:1808px;text-align:center;padding-left:160px;font-size:13px;line-height:18px;color:#fff}
.btn-view{left:870px;top:1870px;font-size:12px;color:#fff;font-weight:500}

/* featured */
.featured-bg{left:0;top:2000px;width:1200px;height:880px;background:var(--soft)}
.featured-box{left:272px;top:2108px;width:656px;height:720px;background:#fff}

/* newsletter */
.newsletter{left:0;top:2880px;width:1200px;height:120px;background:var(--green)}
.nl-title{left:240px;top:2910px;font-size:26px;color:#fff;font-weight:300}
.nl-sub{left:240px;top:2946px;font-size:11px;color:#eaf4de}
.nl-input{left:480px;top:2922px;width:262px;height:34px;border-bottom:1px solid rgba(255,255,255,.7);color:#fff;font-size:11px;padding:12px 8px}
.nl-btn{left:742px;top:2924px;width:118px;height:32px;background:#fff;color:var(--ink);font-size:10px;font-weight:700;display:flex;align-items:center;justify-content:center;letter-spacing:.5px}
.socials{left:880px;top:2933px;display:flex;gap:8px}
.socials span{width:14px;height:14px;border-radius:50%;background:#fff;opacity:.85}

/* footer */
.site-footer{left:0;top:3000px;width:1200px;height:192px;background:var(--footer)}
.f-col h4{color:#fff;font-size:11px;font-weight:700;letter-spacing:.5px;margin-bottom:12px}
.f-col li{list-style:none;color:var(--footer-text);font-size:10px;line-height:18px;display:flex;align-items:center;gap:8px}
.insta{display:grid;grid-template-columns:repeat(4,36px);gap:8px}
.insta span{width:36px;height:36px}
.copyright{left:240px;top:3160px;font-size:9px;color:var(--footer-text)}
.legal{left:820px;top:3160px;display:flex;gap:20px;font-size:9px;color:var(--footer-text)}
</style>
</head>
<body>

<header class="site-header abs">
  <div class="logo abs">Kolbavi Store<span class="mark"></span></div>
  <nav class="main-nav abs"><a class="active" href="#">Home</a><a href="#">Shop</a><a href="#">Page</a><a href="#">Contact</a></nav>
  <div class="header-icons abs">
    <svg width="14" height="14" viewBox="0 0 14 14" fill="none" stroke="#555" stroke-width="1.4"><circle cx="7" cy="4.5" r="3"/><path d="M1.5 13c.8-3 3-4.2 5.5-4.2S11.7 10 12.5 13"/></svg>
    <svg width="14" height="14" viewBox="0 0 14 14" fill="none" stroke="#555" stroke-width="1.4"><circle cx="6" cy="6" r="4.3"/><path d="M9.2 9.2 13 13"/></svg>
    <svg width="16" height="14" viewBox="0 0 16 14" fill="none" stroke="#555" stroke-width="1.4"><path d="M1 1h2.5l1.8 8h8l1.7-6H4.2"/><circle cx="6" cy="12.3" r="1"/><circle cx="12" cy="12.3" r="1"/></svg>
  </div>
</header>

<section class="hero abs" role="img" aria-label="Woman relaxing with a natural face mask beside leaves and a bowl of skincare cream"></section>
<div class="hero-title abs script">Natural Skincare</div>
<div class="hero-sub abs">Lorem ipsum is simply dummy<br><strong>Lorem ipsum is simply dummy text of printing</strong></div>
<div class="btn-shop abs">Shop Now</div>

<section class="categories">
  <div class="tile abs" style="left:20px;top:556px;width:196px;height:200px;background:var(--tile-blue);justify-content:flex-start;padding-top:36px">Lorem Ipsum<br>Product Name</div>
  <div class="tile abs" style="left:220px;top:556px;width:196px;height:200px;background:var(--tile-lime);justify-content:flex-start;padding-top:36px">Lorem Ipsum<br>Product Name</div>
  <div class="tile big abs" style="left:20px;top:760px;width:396px;height:200px;background:var(--tile-peach);align-items:center;text-align:center;color:var(--ink);font-size:20px">Lorem Ipsum<br>Product Name</div>
  <div class="tile tile-photo abs" role="img" aria-label="Bars of handmade natural soap stacked with herbs" style="left:424px;top:556px;width:352px;height:404px">Lorem Ipsum<br>Product Name</div>
  <div class="tile big abs" style="left:784px;top:556px;width:396px;height:196px;background:var(--tile-mint);align-items:flex-end;text-align:right">Lorem Ipsum<br>Product Name</div>
  <div class="tile abs" style="left:784px;top:756px;width:196px;height:204px;background:var(--tile-lime);justify-content:flex-start;padding-top:36px">Lorem Ipsum<br>Product Name</div>
  <div class="tile abs" style="left:984px;top:756px;width:196px;height:204px;background:var(--tile-pink);justify-content:flex-start;padding-top:36px">Lorem Ipsum<br>Product Name</div>
</section>

<h2 class="section-title abs" style="top:1018px">Best Sellers</h2>
<section class="best-sellers">
  <div class="product abs" style="left:240px;top:1084px">
    <div class="thumb" style="background:var(--tile-lime)"><span class="sale">SALE</span></div>
    <div class="name">Product Name</div><div class="stars">★★★★★</div>
    <div class="price"><b>$45.00</b><s>$60.00</s><span class="cart-dot"><svg width="10" height="10" viewBox="0 0 16 14" fill="none" stroke="#fff" stroke-width="2"><path d="M1 1h2.5l1.8 8h8l1.7-6H4.2"/></svg></span></div>
  </div>
  <div class="product abs" style="left:424px;top:1084px">
    <div class="thumb" style="background:var(--tile-beige)"><div class="hover-frame"></div><span class="btn-cart">Add to cart</span></div>
    <div class="name">Product Name</div><div class="stars">★★★★★</div>
    <div class="price"><b>$45.00</b></div>
  </div>
  <div class="product abs" style="left:608px;top:1084px">
    <div class="thumb" style="background:var(--tile-pink)"></div>
    <div class="name">Product Name</div><div class="stars">★★★★★</div>
    <div class="price"><b>$45.00</b></div>
  </div>
  <div class="product abs" style="left:792px;top:1084px">
    <div class="thumb" style="background:var(--tile-mint)"><span class="sale">SALE</span></div>
    <div class="name">Product Name</div><div class="stars">★★★★★</div>
    <div class="price"><b>$45.00</b><s>$60.00</s></div>
  </div>
</section>
<div class="dots abs"><span class="on"></span><span></span><span></span></div>

<section class="banner abs" role="img" aria-label="Smiling woman touching her face among soft green foliage"></section>
<div class="banner-kicker abs">NEW ARRIVALS</div>
<div class="banner-title abs script">Natural Skincare</div>
<div class="banner-copy abs">Lorem ipsum is simply dummy text of the printing and typesetting<br>industry. Lorem ipsum has been the standard dummy text ever since.</div>
<div class="btn-view abs">View Product</div>

<div class="featured-bg abs"></div>
<h2 class="section-title abs" style="top:2052px;width:auto;left:240px;font-size:24px">Featured products</h2>
<div class="featured-box abs"></div>
<section class="featured">
  <div class="product abs" style="left:292px;top:2128px;width:180px"><div class="thumb" style="width:180px;height:192px;background:var(--tile-blue)"></div><div class="name">Product Name</div><div class="stars">★★★★★</div><div class="price"><b>$45.00</b></div></div>
  <div class="product abs" style="left:510px;top:2128px;width:180px"><div class="thumb" style="width:180px;height:192px;background:var(--tile-lime)"><span class="sale">SALE</span></div><div class="name">Product Name</div><div class="stars">★★★★★</div><div class="price"><b>$45.00</b><s>$60.00</s></div></div>
  <div class="product abs" style="left:728px;top:2128px;width:180px"><div class="thumb" style="width:180px;height:192px;background:var(--tile-mint)"><span class="sale">SALE</span></div><div class="name">Product Name</div><div class="stars">★★★★★</div><div class="price"><b>$45.00</b><s>$60.00</s></div></div>
  <div class="product abs" style="left:292px;top:2412px;width:180px"><div class="thumb" style="width:180px;height:192px;background:var(--tile-lime)"><span class="sale">SALE</span></div><div class="name">Product Name</div><div class="stars">★★★★★</div><div class="price"><b>$45.00</b><s>$60.00</s><span class="cart-dot"><svg width="10" height="10" viewBox="0 0 16 14" fill="none" stroke="#fff" stroke-width="2"><path d="M1 1h2.5l1.8 8h8l1.7-6H4.2"/></svg></span></div></div>
  <div class="product abs" style="left:510px;top:2412px;width:180px"><div class="thumb" style="width:180px;height:192px;background:var(--tile-mint)"><div class="hover-frame" style="background:#fff;inset:14px;border:none"></div><span class="btn-cart" style="left:40px;top:26px">Add to cart</span></div><div class="name">Product Name</div><div class="stars">★★★★★</div><div class="price"><b>$45.00</b></div></div>
  <div class="product abs" style="left:728px;top:2412px;width:180px"><div class="thumb" style="width:180px;height:192px;background:var(--tile-pink)"></div><div class="name">Product Name</div><div class="stars">★★★★★</div><div class="price"><b>$45.00</b></div></div>
</section>

<section class="newsletter abs"></section>
<div class="nl-title abs">Our Newsletter</div>
<div class="nl-sub abs">Get the latest news and offers</div>
<div class="nl-input abs">Email address</div>
<div class="nl-btn abs">SUBSCRIBE NOW</div>
<div class="socials abs"><span></span><span></span><span></span><span></span></div>

<footer class="site-footer abs"></footer>
<div class="f-col abs" style="left:240px;top:3028px">
  <h4>CONTACT INFO</h4>
  <ul>
    <li><svg width="9" height="11" viewBox="0 0 10 12" fill="var(--green)"><path d="M5 0a4 4 0 0 0-4 4c0 3 4 8 4 8s4-5 4-8a4 4 0 0 0-4-4zm0 5.5A1.5 1.5 0 1 1 5 2.5a1.5 1.5 0 0 1 0 3z"/></svg>12 Fernleaf Road, Greenhill</li>
    <li><svg width="10" height="10" viewBox="0 0 12 12" fill="var(--green)"><path d="M2.5 0 5 2.8 3.6 4.3a7 7 0 0 0 4 4L9.2 7 12 9.5 10.5 12C4.7 12 0 7.3 0 1.5z"/></svg>+00 123 456 789</li>
    <li><svg width="11" height="9" viewBox="0 0 12 9" fill="none" stroke="var(--green)" stroke-width="1.3"><rect x=".6" y=".6" width="10.8" height="7.8"/><path d="m.6.6 5.4 4.3L11.4.6"/></svg>hello@kolbavi.co</li>
    <li>Mon – Fri, 9am – 6pm</li>
  </ul>
</div>
<div class="f-col abs" style="left:480px;top:3028px"><h4>INFORMATION</h4><ul><li>About Us</li><li>Delivery</li><li>Returns</li><li>Privacy</li><li>Terms</li></ul></div>
<div class="f-col abs" style="left:608px;top:3028px"><h4>USEFUL LINKS</h4><ul><li>Face</li><li>Body</li><li>Baby</li><li>Ingredients</li></ul></div>
<div class="f-col abs" style="left:740px;top:3028px">
  <h4>INSTAGRAM</h4>
  <div class="insta" role="img" aria-label="Grid of product photos from the social feed">
    <span style="background:var(--tile-lime)"></span><span style="background:var(--tile-pink)"></span><span style="background:var(--tile-blue)"></span><span style="background:var(--tile-mint)"></span>
    <span style="background:var(--tile-mint)"></span><span style="background:var(--tile-peach)"></span><span style="background:var(--tile-lime)"></span><span style="background:var(--tile-pink)"></span>
  </div>
</div>
<div class="copyright abs">© 2024 Kolbavi store.co</div>
<div class="legal abs"><span>Privacy</span><span>Terms</span><span>Sitemap</span><span>Help</span></div>

</body>
</html>
```